Fruits and Vegetables distribution company needs a new eye catching website

We need to get our website up to date. Our clients will look at our website to learn about our products and services. Our design needs to be simple yet impactful to make our brand memorable to our visitors. We need to have somewhere to tell our clients about our history, products and services, our team. We can throw in a few fun facts and figures and maybe some testimonials to impress. We have 4 theme colors that we want to incorporate into the design, you can get in touch for the HEX/RGB codes. Please remember that smooth operation of any animations and interactions is very important.

Need extra days to review

```html
<!DOCTYPE html>
<html lang="en">
<head>
<meta charset="utf-8">
<title>Freska Farm General Trading LLC</title>
<link href="https://fonts.googleapis.com/css2?family=Roboto:wght@300;400;500;700&display=swap" rel="stylesheet">
<style>
:root{
  --green:#8dc63f;
  --green-dark:#6fa82a;
  --orange:#f7a800;
  --red:#c8302f;
  --gray-card:#d9d9d9;
  --text:#333333;
  --text-soft:#555555;
  --white:#ffffff;
  --black:#111111;
  --field:#3b3b3b;
}
*{box-sizing:border-box;margin:0;padding:0}
html,body{width:1200px;height:3364px;overflow:hidden}
body{position:relative;font-family:'Roboto',Arial,sans-serif;color:var(--text);background:var(--white)}
.abs{position:absolute}
.center{text-align:center}

.topbar{left:0;top:0;width:1200px;height:40px;display:flex;justify-content:flex-end;align-items:center;gap:36px;padding-right:28px;font-size:15px;color:var(--green-dark)}
.topbar span{display:flex;align-items:center;gap:10px}
.header{left:0;top:40px;width:1200px;height:113px;background:var(--green);border-bottom:4px solid var(--orange)}
.brand{left:27px;top:26px;font-size:52px;font-weight:700;color:var(--white);letter-spacing:1px}
.nav{right:28px;top:42px;display:flex;font-size:15px;font-weight:700;color:var(--white)}
.nav a{padding:0 24px;border-left:2px solid var(--white);line-height:34px}
.nav a:first-child{border-left:none}

.hero{left:0;top:157px;width:1200px;height:449px;background:linear-gradient(120deg,#6b8f2a 0%,#c9641d 30%,#e0a21a 55%,#9b1e14 78%,#4c6b22 100%)}
.hero-title{left:0;top:295px;width:1200px;font-size:50px;font-weight:700;color:var(--white);text-shadow:0 2px 6px rgba(0,0,0,.5)}
.hero-slogan{left:0;top:404px;width:1200px;font-size:20px;color:var(--white);text-shadow:0 1px 4px rgba(0,0,0,.6)}
.hero-btn{left:523px;top:520px;width:219px;height:59px;background:var(--green);border-radius:8px;color:var(--white);font-size:20px;font-weight:700;line-height:59px}

.section-title{left:0;width:1200px;font-size:40px;font-weight:700;color:var(--green)}
.section-lead{left:90px;width:1020px;font-size:16px;line-height:22px;color:var(--text)}
.rule{left:516px;width:168px;height:3px;background:var(--orange)}

.card{background:var(--gray-card)}
.card .photo{width:100%}
.card h3{font-size:18px;font-weight:700;color:var(--green);margin:18px 0 14px 18px}
.card p{font-size:15px;line-height:20px;color:var(--text);margin:0 18px}

.about{left:0;top:1525px;width:1200px;height:801px;background:var(--green)}
.about-title{left:0;top:1563px;width:1200px;font-size:40px;font-weight:700;color:var(--white)}
.sub-title{font-size:42px;font-weight:700;color:var(--white)}
.red-rule{height:3px;background:var(--red)}
.about-text{font-size:16px;line-height:22px;color:#263014}
.achieve{left:733px;top:1653px;width:467px;height:673px;background:var(--orange)}

.person .avatar{width:123px;height:123px;border-radius:50%;background:radial-gradient(circle,#c9c9c9,#8c8c8c);margin:0 auto}
.person .name{font-size:16px;margin-top:20px;color:var(--text)}
.person .stars{margin-top:6px}
.person .quote{font-size:16px;line-height:20px;margin-top:12px;color:var(--text)}

.footer{left:0;top:2905px;width:1200px;height:386px;background:var(--green)}
.foot-head{font-size:18px;font-weight:500;color:var(--red)}
.foot-text{font-size:15px;line-height:19px;color:var(--white)}
.quick li{list-style:none;font-size:16px;color:var(--white);height:38px}
.post-title{font-size:18px;font-weight:700;color:var(--white)}
.post-date{font-size:15px;color:var(--white)}
.field{left:902px;width:255px;height:41px;background:var(--field);border-radius:6px;color:#dddddd;font-size:16px;line-height:41px;padding-left:18px}
.submit{left:902px;top:3246px;width:130px;height:29px;background:var(--red);color:var(--white);font-size:15px;line-height:29px;text-align:center}
.copyright{left:0;top:3291px;width:1200px;height:73px;background:var(--black);color:#cccccc;font-size:15px;line-height:73px;padding-left:27px}
</style>
</head>
<body>

<div class="abs topbar">
  <span><svg width="20" height="20" viewBox="0 0 24 24"><path fill="#c8302f" d="M6.6 10.8a15 15 0 0 0 6.6 6.6l2.2-2.2c.3-.3.7-.4 1-.2 1.1.4 2.3.6 3.6.6.6 0 1 .4 1 1V20c0 .6-.4 1-1 1A17 17 0 0 1 3 4c0-.6.4-1 1-1h3.5c.6 0 1 .4 1 1 0 1.3.2 2.5.6 3.6.1.3 0 .7-.2 1z"/></svg>+971 (4) 555-0142</span>
  <span><svg width="32" height="22" viewBox="0 0 32 22"><rect x="1" y="1" width="30" height="20" fill="none" stroke="#c8302f" stroke-width="2"/><path d="M1 1l15 11L31 1" fill="none" stroke="#c8302f" stroke-width="2"/></svg>info@freskaproduce.com</span>
</div>

<header class="abs header">
  <div class="abs brand">FRESKA</div>
  <nav class="abs nav"><a>PRODUCTS AND SERVICES</a><a>ABOUT US</a><a>CONTACTS</a></nav>
</header>

<div class="abs hero" role="img" aria-label="Photo of assorted fresh fruits and vegetables"></div>
<h1 class="abs hero-title center">FRESKA FARM GENERAL TRADING LLC</h1>
<div class="abs hero-slogan center">SOMETHING ABOUT THE COMPANY AND WHAT WE DO SLOGAN</div>
<div class="abs hero-btn center">GET A QUOTE NOW</div>

<h2 class="abs section-title center" style="top:645px">PRODUCTS &amp; SERVICES</h2>
<p class="abs section-lead center" style="top:708px">Lorem ipsum dolor sit amet, consectetur adipiscing elit. Nulla aliquet vestibulum orci, quis maximus tellus tincidunt nec. Aliquam ullamcorper sapien at ex condimentum viverra</p>
<div class="abs rule" style="top:780px"></div>

<div class="abs card" style="left:25px;top:857px;width:269px;height:316px">
  <div class="photo" role="img" aria-label="Photo of carrots" style="height:168px;background:linear-gradient(135deg,#e0621a,#c04a10)"></div>
  <h3>PRODUCT 1</h3><p>Dignissimmorbi rhoncus sed netus ligula consecue netus nulla aliquat id dui.</p>
</div>
<div class="abs card" style="left:318px;top:857px;width:272px;height:316px">
  <div class="photo" role="img" aria-label="Photo of lemons" style="height:168px;background:linear-gradient(135deg,#f2e02a,#d6b80e)"></div>
  <h3>PRODUCT 2</h3><p>Dignissimmorbi rhoncus sed netus ligula consecue netus nulla aliquat id dui.</p>
</div>
<div class="abs card" style="left:612px;top:857px;width:269px;height:316px">
  <div class="photo" role="img" aria-label="Photo of bananas" style="height:168px;background:linear-gradient(135deg,#f0d53a,#b89a1c)"></div>
  <h3>PRODUCT 3</h3><p>Dignissimmorbi rhoncus sed netus ligula consecue netus nulla aliquat id dui.</p>
</div>
<div class="abs card" style="left:906px;top:857px;width:269px;height:316px">
  <div class="photo" role="img" aria-label="Photo of tomatoes" style="height:168px;background:linear-gradient(135deg,#d42a1c,#8e140c)"></div>
  <h3>PRODUCT 4</h3><p>Dignissimmorbi rhoncus sed netus ligula consecue netus nulla aliquat id dui.</p>
</div>

<div class="abs card" style="left:25px;top:1225px;width:565px;height:262px">
  <div class="photo" role="img" aria-label="Photo of mixed vegetables and fruits" style="height:143px;background:linear-gradient(90deg,#5b8a2a,#d0641a,#c2261a,#7da22e)"></div>
  <h3>SERVICE 1</h3><p>Proin quis lacinia sem. Nunc libero est, pretium sit amet lorem eget, vehicula soll icitudin lorem. Pellentesque posuere,</p>
</div>
<div class="abs card" style="left:612px;top:1225px;width:563px;height:262px">
  <div class="photo" role="img" aria-label="Photo of fruit display" style="height:143px;background:linear-gradient(90deg,#a4231a,#e8a020,#7a9a2a,#b6201a)"></div>
  <h3>SERVICE 1</h3><p>Proin quis lacinia sem. Nunc libero est, pretium sit amet lorem eget, vehicula soll icitudin lorem. Pellentesque posuere,</p>
</div>

<section class="abs about"></section>
<h2 class="abs about-title center">ABOUT US</h2>

<h3 class="abs sub-title" style="left:27px;top:1665px">WHO WE ARE</h3>
<div class="abs red-rule" style="left:27px;top:1726px;width:175px"></div>
<p class="abs about-text" style="left:27px;top:1744px;width:680px">Proin quis lacinia sem. Nunc libero est, pretium sit amet lorem eget, vehicula soll icitudin lorem. Pellentesque posuere, ligula quis tempus euismod, libero magna i nterdum leo, vitae viverra sem arcu ut neque. Ut suscipit ipsum urna. Morbi impe rdiet tempor mauris et scelerisque. Nam tincidunt, magna sit amet tempor ultric ies, lorem tellus porta turpis, a hendrerit leo nulla ac nisi. Nam interdum ullamcor per turpis at consequat. In non quam ullamcorper elit varius vehicula in a ante. Nulla pharetra efficitur semper. Proin ut ligula nec purus vulputate tristique. Pelle ntesque diam leo, dapibus et lacus eget, interdum congue massa. Etiam finibus l uctus scelerisque.</p>

<h3 class="abs sub-title" style="left:27px;top:1994px">OUR TEAM</h3>
<div class="abs red-rule" style="left:27px;top:2056px;width:175px"></div>
<div class="abs" role="img" aria-label="Illustration of a team holding hands" style="left:27px;top:2082px;width:702px;height:244px;background:linear-gradient(180deg,#f2f4f6,#aab4bc)"></div>

<aside class="abs achieve"></aside>
<h3 class="abs sub-title" style="left:758px;top:1665px">ACHIEVEMENTS</h3>
<div class="abs red-rule" style="left:758px;top:1726px;width:175px"></div>
<div class="abs" role="img" aria-label="Photo of an achievement award trophy" style="left:758px;top:1747px;width:395px;height:178px;background:linear-gradient(135deg,#0d2a4a,#1f5c8c 60%,#0b1f38)"></div>
<p class="abs about-text" style="left:758px;top:1955px;width:430px;color:var(--white)">Proin quis lacinia sem. Nunc libero est, pretium sit amet lorem eget, vehicula soll icitudin lorem. Pellentesque posuere, ligula quis tempus euismod, libero magna i nterdum leo, vitae viverra sem arcu ut neque. Ut suscipit ipsum urna.</p>
<p class="abs about-text" style="left:758px;top:2115px;width:430px;color:var(--white)">Morbi impe rdiet tempor mauris et scelerisque. Nam tincidunt, magna sit amet tempor ultric ies, e.</p>
<div class="abs" role="img" aria-label="Award badge" style="left:888px;top:2169px;width:99px;height:144px;background:#1a1a1a;border-radius:10px"></div>

<h2 class="abs section-title center" style="top:2375px">CLIENT TESTIMONIALS</h2>
<p class="abs section-lead center" style="top:2448px">Lorem Ipsum is that it has a more-or-less normal distribution of letters, as opposed to using 'Content here, content here', making it look like readable English. Many desktop publishing</p>
<div class="abs rule" style="top:2522px"></div>

<svg width="0" height="0" style="position:absolute"><defs><symbol id="star" viewBox="0 0 24 24"><polygon points="12,1 15,9 23,9 17,14 19,23 12,18 5,23 7,14 1,9 9,9" fill="#c8302f"/></symbol></defs></svg>

<div class="abs person center" style="left:89px;top:2575px;width:240px">
  <div class="avatar" role="img" aria-label="Client portrait"></div>
  <div class="name">ADAM</div>
  <div class="stars"><svg width="34" height="34"><use href="#star"/></svg><svg width="34" height="34"><use href="#star"/></svg><svg width="34" height="34"><use href="#star"/></svg><svg width="34" height="34"><use href="#star"/></svg><svg width="34" height="34"><use href="#star"/></svg></div>
  <div class="quote">"Contrary to popular belief, Lorem Ipsum is not simply random text. Contrary to popular."</div>
</div>
<div class="abs person center" style="left:479px;top:2575px;width:240px">
  <div class="avatar" role="img" aria-label="Client portrait"></div>
  <div class="name">ADAM</div>
  <div class="stars"><svg width="34" height="34"><use href="#star"/></svg><svg width="34" height="34"><use href="#star"/></svg><svg width="34" height="34"><use href="#star"/></svg><svg width="34" height="34"><use href="#star"/></svg><svg width="34" height="34"><use href="#star"/></svg></div>
  <div class="quote">"Contrary to popular belief, Lorem Ipsum is not simply random text. Contrary to popular"</div>
</div>
<div class="abs person center" style="left:880px;top:2575px;width:240px">
  <div class="avatar" role="img" aria-label="Client portrait"></div>
  <div class="name">ADAM</div>
  <div class="stars"><svg width="34" height="34"><use href="#star"/></svg><svg width="34" height="34"><use href="#star"/></svg><svg width="34" height="34"><use href="#star"/></svg><svg width="34" height="34"><use href="#star"/></svg><svg width="34" height="34"><use href="#star"/></svg></div>
  <div class="quote">"Contrary to popular belief, Lorem Ipsum is not simply random text. Contrary to popular"</div>
</div>

<footer class="abs footer"></footer>
<div class="abs foot-head" style="left:27px;top:2934px">ABOUT US</div>
<div class="abs brand" style="left:27px;top:3000px;font-size:48px">FRESKA</div>
<p class="abs foot-text" style="left:27px;top:3100px;width:230px">Here are many variations of passages of Lorem Ipsum available, but the majority have suffered alteration in some form, by injected humour, or randomised words which don't look even slightly believa...</p>
<div class="abs" style="left:27px;top:3246px;font-size:15px;color:var(--red)">Read More</div>

<div class="abs foot-head" style="left:316px;top:2934px">QUICK LINK</div>
<ul class="abs quick" style="left:316px;top:2987px">
  <li>Lorem ipsum dolor t 1</li><li>Mauris egestas risus 2</li><li>Nunc efficitur sapien 3</li><li>Ut accumsan felis id 4</li><li>Etiam iaculis eros at 5</li><li>Etiam sed tortor sed 6</li><li>Lorem ipsum dolor t 7</li><li>Mauris egestas risus 8</li>
</ul>

<div class="abs foot-head" style="left:612px;top:2934px">BLOG</div>
<div class="abs post-title" style="left:612px;top:2992px">Post Title</div>
<div class="abs post-date" style="left:612px;top:3015px">Friday, 6th April 2000</div>
<p class="abs foot-text" style="left:612px;top:3052px;width:270px">Nulla dacilisi. Ut fringilla. Sispendia se tpotenti. Nunc Feugiat</p>
<div class="abs" style="left:612px;top:3120px;width:248px;height:2px;background:var(--black)"></div>
<div class="abs post-title" style="left:612px;top:3145px">Post Title</div>
<div class="abs post-date" style="left:612px;top:3168px">Friday, 6th April 2000</div>
<p class="abs foot-text" style="left:612px;top:3205px;width:270px">Nulla dacilisi. Ut fringilla. Sispendia se tpotenti. Nunc Feugiat</p>

<div class="abs foot-head" style="left:902px;top:2934px">CONTACT US</div>
<div class="abs" style="left:902px;top:3004px;display:flex;align-items:center;gap:8px;color:var(--white);font-size:16px;font-weight:500"><svg width="20" height="20" viewBox="0 0 24 24"><path fill="#ffffff" d="M6.6 10.8a15 15 0 0 0 6.6 6.6l2.2-2.2c.3-.3.7-.4 1-.2 1.1.4 2.3.6 3.6.6.6 0 1 .4 1 1V20c0 .6-.4 1-1 1A17 17 0 0 1 3 4c0-.6.4-1 1-1h3.5c.6 0 1 .4 1 1 0 1.3.2 2.5.6 3.6.1.3 0 .7-.2 1z"/></svg>+971 (4) 555-0142</div>
<div class="abs" style="left:902px;top:3052px;display:flex;align-items:center;gap:12px;color:var(--white);font-size:16px;font-weight:500"><svg width="34" height="24" viewBox="0 0 32 22"><rect x="1" y="1" width="30" height="20" fill="none" stroke="#ffffff" stroke-width="2"/><path d="M1 1l15 11L31 1" fill="none" stroke="#ffffff" stroke-width="2"/></svg>info@freskaproduce.com</div>
<div class="abs foot-head" style="left:902px;top:3104px">NEWSLETTER</div>
<div class="abs field" style="top:3142px">Name</div>
<div class="abs field" style="top:3196px">Email</div>
<div class="abs submit">SUBMIT</div>

<div class="abs copyright">Copyright &nbsp;2013 - All Rights Reserved - Domain Name</div>

</body>
</html>
```